Fox & Fig honey company needs a label design.

We need a label design for a new honey company, based in the state of Florida called 'Fox & Fig". We are supplying our online customers with the highest quality of the various kinds of raw honey. Our product is honey in the oval hexagon glass jar with black lid. We would like to see designs that use black background with gold font .
In the upper part of the label is gold flying Honey Bee (profile, silhouette). The name of the brand "Fox & Fig" - Caramel font. Additional fonts are Cinzel, Source Sans Pro. Label measurements 2.6" by 3".
Label content:
Fox & Fig
RAW HONEY
wildflower
PURE & NATURAL
made by Florida Bees
foxandfigjars.com
NET WT 12oz (340g)

The final design should have eye catching, luxurious look.
Updates

Need extra days to review

Target Market(s)

Luxury

Industry/Entity Type

Food (bee products)

Font styles to use
Other font styles liked:
• caramel

Colors

Designer to choose colors to be used in the design.

Requirements
Must have
• Gold letters on black background, Drawing of a bee, flying in profile

```html
<!DOCTYPE html>
<html lang="en">
<head>
<meta charset="utf-8">
<title>Fox &amp; Fig Raw Honey Label</title>
<link href="https://fonts.googleapis.com/css2?family=Cinzel:wght@400;700&family=Josefin+Sans:wght@600&display=swap" rel="stylesheet">
<style>
  :root {
    --label-black: #000000;
    --gold: #e9a21f;
    --gold-light: #f2b634;
    --cream: #f7efe2;
    --amber-deep: #3a2306;
    --amber-mid: #8a5410;
    --panel-dark: #0d0906;
  }
  html, body {
    margin: 0;
    padding: 0;
    width: 1200px;
    height: 1040px;
    overflow: hidden;
    background: var(--label-black);
  }
  .label {
    position: relative;
    width: 1200px;
    height: 1040px;
    background: var(--label-black);
    overflow: hidden;
  }
  .honey-visual {
    position: absolute;
    left: 208px;
    top: 253px;
    width: 784px;
    height: 787px;
    background:
      radial-gradient(ellipse 42% 34% at 50% 40%, var(--amber-mid) 0%, var(--amber-deep) 55%, rgba(20,12,4,0) 100%),
      radial-gradient(ellipse 40% 10% at 50% 80%, #2a1a08 0%, rgba(0,0,0,0) 100%),
      linear-gradient(180deg, var(--panel-dark) 0%, #1a1108 50%, var(--panel-dark) 100%);
  }
  .frame {
    position: absolute;
    inset: 0;
  }
  .brand-name {
    position: absolute;
    left: 0;
    right: 0;
    top: 78px;
    text-align: center;
    font-family: "Cinzel", serif;
    font-weight: 700;
    font-size: 84px;
    line-height: 100px;
    color: var(--gold);
    margin: 0;
  }
  .product-type {
    position: absolute;
    left: 0;
    right: 0;
    top: 290px;
    text-align: center;
    font-family: "Cinzel", serif;
    font-weight: 700;
    font-size: 62px;
    line-height: 76px;
    color: var(--gold);
    margin: 0;
  }
  .variety-tag {
    position: absolute;
    left: 435px;
    top: 453px;
    width: 330px;
    height: 72px;
  }
  .variety-tag svg { position: absolute; inset: 0; }
  .variety-name {
    position: absolute;
    inset: 0;
    display: flex;
    align-items: center;
    justify-content: center;
    font-family: "Josefin Sans", sans-serif;
    font-weight: 600;
    font-size: 36px;
    padding-top: 6px;
    color: var(--cream);
    letter-spacing: 1px;
  }
  .claim {
    position: absolute;
    left: 0;
    right: 0;
    top: 570px;
    text-align: center;
    font-family: "Cinzel", serif;
    font-weight: 400;
    font-size: 60px;
    line-height: 62px;
    color: var(--cream);
    margin: 0;
  }
  .origin, .website {
    position: absolute;
    left: 0;
    right: 0;
    text-align: center;
    font-family: "Josefin Sans", sans-serif;
    font-weight: 600;
    font-size: 30px;
    margin: 0;
  }
  .origin { top: 772px; color: var(--gold-light); }
  .website { top: 818px; color: var(--cream); }
  .net-weight {
    position: absolute;
    left: 419px;
    top: 896px;
    width: 362px;
    height: 60px;
  }
  .net-weight svg { position: absolute; inset: 0; }
  .net-weight-text {
    position: absolute;
    inset: 0;
    display: flex;
    align-items: center;
    justify-content: center;
    padding-top: 4px;
    font-family: "Josefin Sans", sans-serif;
    font-weight: 600;
    font-size: 31px;
    color: var(--label-black);
  }
</style>
</head>
<body>
<main class="label">
  <div class="honey-visual" role="img" aria-label="Honeycomb piece with golden honey dripping into a glossy pool"></div>

  <svg class="frame" width="1200" height="1040" viewBox="0 0 1200 1040" aria-hidden="true">
    <path d="M 355 128 L 165 128 A 53 53 0 0 1 112 181 L 112 870 A 53 53 0 0 1 165 923 L 1035 923 A 53 53 0 0 1 1088 870 L 1088 181 A 53 53 0 0 1 1035 128 L 845 128"
          fill="none" stroke="var(--gold)" stroke-width="5"/>
  </svg>

  <h1 class="brand-name">Fox &amp; Fig</h1>

  <h2 class="product-type">RAW HONEY</h2>

  <div class="variety-tag">
    <svg width="330" height="72" viewBox="0 0 330 72" aria-hidden="true">
      <polygon points="14,3 316,3 327,14 327,58 316,69 14,69 3,58 3,14" fill="rgba(0,0,0,0.35)" stroke="var(--gold)" stroke-width="4"/>
    </svg>
    <span class="variety-name">WILDFLOWER</span>
  </div>

  <p class="claim">PURE &amp;<br>NATURAL</p>

  <p class="origin">MADE BY FLORIDA BEES</p>
  <p class="website">FOXANDFIGJARS.COM</p>

  <div class="net-weight">
    <svg width="362" height="60" viewBox="0 0 362 60" aria-hidden="true">
      <polygon points="12,0 350,0 362,12 362,48 350,60 12,60 0,48 0,12" fill="var(--gold)"/>
    </svg>
    <span class="net-weight-text">NET WT 12oz (340g)</span>
  </div>
</main>
</body>
</html>
```